WTF!!! We need a modern professional website for a business litigation law firm.

We need a modern, clean, professional and uncomplicated website for a new business trial and litigation law firm called "Harrowgate Trial Firm PLLC". Website must be mobile optimized for iPad and smartphone. The law firm specializes in counseling and representing large corporations, small businesses and entrepreneurs in and out of the courtroom. Lawyers in the firm serve as Florida counsel and trial counsel to organizations facing claims involving product liability, premises liability, professional liability, vehicle and transportation liability, warranty claims, construction defects and delay claims, complex business disputes, commercial litigation and bid disputes in State and Federal Courts. The website is mainly to provide information about the firm, and should include sections describing the firm, identifying the Industries Served and Areas of Practice ," a separate page identifying the "Professionals", a separate page for "Resources & Advisories," and a traveling "Connect With Us" button a site visitor can click on that will launch an email to the Firm's general email account. The website should allow us to easily modify the content on these pages, and let us add/modify links to external information sources. We will not sell anything or take payments through the website. We do need to be able to easily upload and update photographs of attorneys and add new attorneys names/email hyperlinks as the firm grows. We would like to add developments in the law or success stories easily and quickly, such as through a blog page. On the "Connect With Us" page the website should have hyperlinks to email the Firm, and there should be hyperlinks to email each professional on the "Professionals" page. The website should be viewable on mobile devices without distortion. The law firm focuses on trial work and should have some imagery associated with courtrooms, but the overall theme of the site should be modern, clean, and communicate sophistication and strength. The website should be made in Wordpress. We have uploaded logo files for Harrowgate Trial Firm.

Target Market(s)

Corporations and companies that are looking for legal representation. Other attorneys/legal industry.

Industry/Entity Type

Legal Industry

Coding

Coded - Design and coding required

Number of Pages Required

1 page

Font styles to use
Sans Serif

Requirements
Must have
• Simple, clean, sophisticated, modern website that includes the logo, watermark of logo, and the elements described above.
Nice to have
• Pictures of city scape, buildings, courtroom, team members.

```html
<!DOCTYPE html>
<html lang="en">
<head>
<meta charset="utf-8">
<title>Harrowgate Trial Firm PLLC</title>
<link rel="stylesheet" href="https://fonts.googleapis.com/css2?family=Rubik:wght@400;500;600;700;800&display=swap">
<style>
:root{
  --red:#d0302a;
  --red-dark:#a8201b;
  --ink:#1e1e1e;
  --dark:#1b1b1d;
  --grey:#f2f2f2;
  --card:#efefef;
  --text:#333;
  --muted:#8a8a8a;
  --white:#fff;
}
*{box-sizing:border-box;margin:0;padding:0}
html,body{width:1200px;height:3750px;overflow:hidden}
body{font-family:'Rubik',sans-serif;color:var(--text);background:var(--white);position:relative}
.abs{position:absolute}
.btn{display:inline-block;background:var(--red);color:var(--white);font-size:11px;font-weight:600;letter-spacing:.5px;text-transform:uppercase;text-align:center;text-decoration:none}
.link-more{color:var(--red);font-size:11px;font-weight:600;display:inline-flex;align-items:center;gap:5px;text-transform:uppercase}
.section-title{font-size:31px;font-weight:600;color:var(--ink);text-align:center;text-transform:uppercase;letter-spacing:.2px}

/* hero */
.hero{left:0;top:0;width:1200px;height:640px;background:linear-gradient(180deg,#2d3240 0%,#3b3b44 40%,#51473f 70%,#3a3634 100%)}
.hero-photo{left:0;top:0;width:1200px;height:640px;background:radial-gradient(ellipse at 50% 40%,rgba(120,110,100,.45),rgba(20,22,30,.2) 70%)}
.hero-fade{left:0;top:560px;width:1200px;height:120px;background:linear-gradient(180deg,rgba(255,255,255,0),#fff)}
.brand{left:121px;top:14px;width:110px;text-align:center;color:var(--white)}
.brand-mark{width:30px;height:30px;border:2px solid var(--white);margin:0 auto 6px}
.brand-name{font-size:19px;font-weight:700;letter-spacing:.3px}
.brand-sub{font-size:7px;letter-spacing:2px;font-weight:500}
.nav{left:302px;top:36px;display:flex;gap:27px;font-size:11px;font-weight:500;color:var(--white)}
.nav .active{color:var(--red)}
.call{left:780px;top:27px;display:flex;align-items:center;gap:8px;color:var(--white)}
.call-icon{width:28px;height:28px;border-radius:50%;background:#000;display:flex;align-items:center;justify-content:center}
.call small{display:block;font-size:9px}
.call strong{font-size:16px;font-weight:600}
.nav-cta{left:943px;top:25px;width:134px;height:34px;line-height:34px}
.hero-title{left:0;top:370px;width:1200px;text-align:center;color:var(--white)}
.hero-title h1{font-size:90px;font-weight:800;line-height:1;letter-spacing:2px}
.hero-title h2{font-size:44px;font-weight:700;letter-spacing:5px;margin-top:6px}
.hero-title p{font-size:15px;font-weight:500;letter-spacing:1.6px;margin-top:18px}

/* connect bar */
.connect{left:121px;top:592px;width:956px;height:83px;background:#0e0e0e;border-top:2px solid var(--red)}
.connect-label{left:0;top:0;width:210px;height:81px;background:var(--red);clip-path:polygon(0 0,100% 0,84% 100%,0 100%);display:flex;align-items:center;gap:14px;padding-left:20px;color:var(--white);font-size:18px;font-weight:600;line-height:1.1;text-transform:uppercase}
.fields{left:198px;top:24px;display:flex;gap:9px}
.field{width:146px;height:33px;background:#2e2e2e;clip-path:polygon(10px 0,100% 0,calc(100% - 10px) 100%,0 100%);color:#ddd;font-size:11px;padding:11px 0 0 20px}
.connect-btn{left:820px;top:24px;width:120px;height:31px;line-height:31px}

/* practice */
.practice-head{left:0;top:718px;width:1200px;text-align:center}
.practice-head p{font-size:11px;color:#444;margin-top:6px}
.grid{left:121px;top:800px;width:956px;display:grid;grid-template-columns:repeat(4,1fr);gap:10px 0}
.card{height:215px;background:var(--card);text-align:center;padding-top:24px;margin-right:8px}
.card:nth-child(4n){margin-right:0}
.card-icon{width:86px;height:86px;border-radius:50%;background:var(--red);margin:0 auto 14px;display:flex;align-items:center;justify-content:center}
.card h3{font-size:15px;font-weight:500;color:var(--ink);text-transform:uppercase;line-height:1.2;height:56px;letter-spacing:.3px}
.card .link-more{margin-top:4px}
.services-btn{left:523px;top:1271px;width:154px;height:37px;line-height:37px}
.watermark{left:0;top:1318px;width:1200px;text-align:center;font-size:70px;font-weight:800;color:#ececec;letter-spacing:0;white-space:nowrap;overflow:hidden;height:65px;line-height:80px}

/* resources */
.resources{left:0;top:1383px;width:1200px;height:546px;background:var(--grey)}
.res-title{left:0;top:45px;width:1200px}
.res-main-img{left:121px;top:102px;width:498px;height:213px;background:linear-gradient(180deg,#9aa7b5 0%,#b8a98a 55%,#5a4a34 100%)}
.res-main{left:121px;top:330px;width:430px}
.date{font-size:10px;color:var(--muted)}
.res-main h3{font-size:14px;font-weight:500;color:var(--ink);margin:8px 0 4px;text-transform:uppercase}
.res-main p{font-size:11px;line-height:1.45;color:#333}
.res-main .link-more{margin-top:14px}
.res-item{left:671px;width:460px;height:100px}
.res-thumb{left:0;top:0;width:165px;height:100px}
.res-text{left:183px;top:5px;width:230px}
.res-text h4{font-size:12px;font-weight:500;color:var(--ink);margin:8px 0 10px;text-transform:uppercase;line-height:1.4}
.res-btn{left:523px;top:458px;width:154px;height:37px;line-height:37px}

/* about */
.about{left:0;top:1929px;width:1200px;height:433px;background:linear-gradient(180deg,#5a5a5a 0%,#3a3a3a 45%,#1f1f1f 100%)}
.about-inner{left:300px;top:160px;width:600px;text-align:center;color:var(--white)}
.about-inner h2{font-size:31px;font-weight:600;text-transform:uppercase}
.about-inner p{font-size:11.5px;line-height:1.55;margin:14px auto 20px;width:510px;color:#e8e8e8}
.about-inner .btn{width:154px;height:37px;line-height:37px}

/* reviews */
.reviews{left:0;top:2362px;width:1200px;height:524px;background:linear-gradient(180deg,#ffffff 0%,#e8eef3 45%,#dfe4e8 62%,#c9ccce 100%)}
.reviews-title{left:0;top:42px;width:1200px}
.avatar{left:557px;top:112px;width:86px;height:86px;border-radius:50%;background:linear-gradient(180deg,#6f7a88,#3f4550);border:4px solid #fff;box-shadow:0 2px 6px rgba(0,0,0,.2)}
.reviewer{left:0;top:222px;width:1200px;text-align:center}
.reviewer h4{font-size:13px;font-weight:500;color:var(--ink)}
.stars{color:var(--red);font-size:15px;letter-spacing:1px}
.reviewer p{width:490px;margin:10px auto 0;font-size:11.5px;line-height:1.55;color:#333}
.arrow-btn{top:190px;width:34px;height:34px;border-radius:50%;background:#4a4a4a;display:flex;align-items:center;justify-content:center}

/* map */
.map{left:0;top:2886px;width:1200px;height:518px;background:linear-gradient(135deg,#eceeed 0%,#e2e6ea 35%,#e9ece6 60%,#e4e8ec 100%)}
.contact-box{left:121px;top:3308px;width:956px;height:191px;background:linear-gradient(180deg,#c92c26,#a71f1b);text-align:center;color:var(--white);padding-top:42px;z-index:5}
.contact-box h2{font-size:29px;font-weight:600;text-transform:uppercase}
.contact-box p{font-size:11px;line-height:1.45;margin:8px auto 14px;width:380px}
.contact-box .btn{background:var(--white);color:var(--ink);width:154px;height:37px;line-height:37px}

/* footer */
.footer{left:0;top:3404px;width:1200px;height:346px;background:var(--dark);color:var(--white);z-index:1}
.footer-inner{left:0;top:132px;width:1200px;height:190px}
.fcol{top:0}
.fcol h5{font-size:14px;font-weight:500;letter-spacing:.8px;text-transform:uppercase;margin-bottom:14px}
.fcol ul{list-style:none;font-size:9px;line-height:2.5}
.fcontact{display:flex;gap:12px;font-size:9px;line-height:1.6;margin-bottom:12px;align-items:center}
.ficon{width:20px;height:20px;border-radius:50%;background:#3a3a3a;flex:none}
.fbrand{left:510px;top:12px;width:180px;text-align:center}
.fbrand .brand-mark{width:44px;height:44px;margin-bottom:10px}
.fbrand .brand-name{font-size:27px}
.fbrand .brand-sub{font-size:12px;letter-spacing:3px}
.social{display:flex;align-items:center;gap:10px;font-size:9px;margin-bottom:14px}
.newsletter p{font-size:9px;line-height:1.6;width:180px;margin-bottom:14px}
.sub-row{display:flex}
.sub-input{width:115px;height:30px;background:#3a3a3a}
.sub-btn{width:76px;height:30px;line-height:30px}
.legal{left:0;top:322px;width:1200px;text-align:center;font-size:8px;color:#ddd}
</style>
</head>
<body>

<!-- Hero -->
<section class="abs hero">
  <div class="abs hero-photo" role="img" aria-label="Team of five attorneys standing with arms crossed in front of a night city skyline"></div>
  <div class="abs hero-fade"></div>
  <div class="abs brand">
    <div class="brand-mark"></div>
    <div class="brand-name">HARROWGATE</div>
    <div class="brand-sub">TRIAL FIRM</div>
  </div>
  <nav class="abs nav">
    <span class="active">HOME</span><span>AREAS OF PRACTICE</span><span>PROFESSIONALS</span><span>RESOURCES &amp; ADVISORIES</span>
  </nav>
  <div class="abs call">
    <div class="call-icon"><svg width="12" height="16" viewBox="0 0 12 16"><rect x="1" y="1" width="10" height="14" rx="2" fill="none" stroke="#d0302a" stroke-width="2"/></svg></div>
    <div><small>CALL US TODAY:</small><strong>954-555-0182</strong></div>
  </div>
  <a class="abs btn nav-cta">Connect with us</a>
  <div class="abs hero-title">
    <h1>HARROWGATE</h1>
    <h2>TRIAL FIRM PLLC</h2>
    <p>A NEW BUSINESS TRIAL AND LITIGATION LAW FIRM</p>
  </div>
</section>

<!-- Connect bar -->
<form class="abs connect">
  <div class="abs connect-label">
    <svg width="38" height="34" viewBox="0 0 38 34"><path d="M2 16 L36 2 L26 32 L18 20 Z" fill="#fff"/><path d="M18 20 L36 2" stroke="#d0302a" stroke-width="2"/></svg>
    <span>Connect<br>with us</span>
  </div>
  <div class="abs fields">
    <div class="field">Name</div><div class="field">Email</div><div class="field">Phone</div>
    <div class="field">Subject <span style="float:right;margin-right:18px">&#8964;</span></div>
  </div>
  <a class="abs btn connect-btn">Let's connect</a>
</form>

<!-- Practice areas -->
<div class="abs practice-head">
  <h2 class="section-title">Industries Served and Areas of Practice</h2>
  <p>Lorem ipsum dolor sit amet, consectetur adipiscing elit. Ut porta feugiat dolor, vel dictum eros. Cras porta diam sed est tincidunt.</p>
</div>
<div class="abs grid">
  <div class="card"><div class="card-icon"><svg width="40" height="40" viewBox="0 0 40 40" fill="#fff"><rect x="8" y="20" width="24" height="16" rx="2"/><circle cx="20" cy="10" r="6"/></svg></div><h3>Product<br>Liability</h3><span class="link-more">Read more &#10230;</span></div>
  <div class="card"><div class="card-icon"><svg width="40" height="40" viewBox="0 0 40 40"><circle cx="20" cy="20" r="14" fill="none" stroke="#fff" stroke-width="3"/><text x="20" y="27" font-size="18" text-anchor="middle" fill="#fff" font-family="Rubik,sans-serif">$</text></svg></div><h3>Premises<br>Liability</h3><span class="link-more">Read more &#10230;</span></div>
  <div class="card"><div class="card-icon"><svg width="40" height="40" viewBox="0 0 40 40" fill="#fff"><path d="M6 10 L16 6 L26 10 V20 C26 28 16 34 16 34 C16 34 6 28 6 20 Z"/><circle cx="30" cy="10" r="4"/><rect x="27" y="16" width="6" height="18"/></svg></div><h3>Professional<br>Liability</h3><span class="link-more">Read more &#10230;</span></div>
  <div class="card"><div class="card-icon"><svg width="40" height="40" viewBox="0 0 40 40"><path d="M20 4 L33 9 V19 C33 28 20 36 20 36 C20 36 7 28 7 19 V9 Z" fill="none" stroke="#fff" stroke-width="3"/><path d="M14 19 L19 24 L27 15" fill="none" stroke="#fff" stroke-width="3"/></svg></div><h3>Warranty<br>Claims</h3><span class="link-more">Read more &#10230;</span></div>
  <div class="card"><div class="card-icon"><svg width="40" height="40" viewBox="0 0 40 40"><circle cx="18" cy="18" r="10" fill="none" stroke="#fff" stroke-width="6" stroke-dasharray="5 3"/><circle cx="30" cy="30" r="7" fill="#fff"/><rect x="29" y="25" width="2" height="6" fill="#d0302a"/></svg></div><h3>Construction<br>Defects &amp; Delay<br>Claims</h3><span class="link-more">Read more &#10230;</span></div>
  <div class="card"><div class="card-icon"><svg width="40" height="40" viewBox="0 0 40 40" stroke="#fff" stroke-width="2.5" fill="none"><path d="M20 6 V32 M8 12 H32 M8 12 L4 22 H12 Z M32 12 L28 22 H36 Z M12 34 H28"/></svg></div><h3>Commercial Litigation<br>&amp; Bid Disputes in State<br>&amp; Federal Courts</h3><span class="link-more">Read more &#10230;</span></div>
  <div class="card"><div class="card-icon"><svg width="40" height="40" viewBox="0 0 40 40" fill="none" stroke="#fff" stroke-width="3"><circle cx="20" cy="20" r="15"/><circle cx="20" cy="20" r="9"/><circle cx="20" cy="20" r="3" fill="#fff"/></svg></div><h3>Complex<br>Business Disputes</h3><span class="link-more">Read more &#10230;</span></div>
  <div class="card"><div class="card-icon"><svg width="40" height="40" viewBox="0 0 40 40" fill="#fff"><path d="M6 20 L10 10 H30 L34 20 V30 H6 Z"/><circle cx="12" cy="25" r="2.5" fill="#d0302a"/><circle cx="28" cy="25" r="2.5" fill="#d0302a"/></svg></div><h3>Vehicle &amp;<br>Transportation<br>Liability</h3><span class="link-more">Read more &#10230;</span></div>
</div>
<a class="abs btn services-btn">View all services</a>
<div class="abs watermark">HARROWGATE TRIAL FIRM PLLC</div>

<!-- Resources -->
<section class="abs resources">
  <h2 class="abs section-title res-title">Latest Resources &amp; Advisories</h2>
  <div class="abs res-main-img" role="img" aria-label="Classical colonnaded courthouse building under a cloudy sky"></div>
  <div class="abs res-main">
    <div class="date">February 28, 2024</div>
    <h3>Pellentesque feugiat, purus vitae maximus finibus.</h3>
    <p>Lorem ipsum dolor sit amet, consectetur adipiscing elit. Ut porta feugiat dolor, vel dictum eros. Cras porta diam sed est tincidunt.</p>
    <span class="link-more">Read more &#10230;</span>
  </div>
  <div class="abs res-item" style="top:102px">
    <div class="abs res-thumb" role="img" aria-label="Judge's gavel resting on open law books" style="background:linear-gradient(135deg,#c9b89c,#6b5a48)"></div>
    <div class="abs res-text"><div class="date">February 28, 2024</div><h4>There are many variations of passages of lorem ipsum.</h4><span class="link-more">Read more &#10230;</span></div>
  </div>
  <div class="abs res-item" style="top:215px">
    <div class="abs res-thumb" role="img" aria-label="Handshake across a desk with a gavel" style="background:linear-gradient(135deg,#cfd5db,#3c4148)"></div>
    <div class="abs res-text"><div class="date">February 28, 2024</div><h4>If you are going to use a passage of lorem ipsum.</h4><span class="link-more">Read more &#10230;</span></div>
  </div>
  <div class="abs res-item" style="top:328px">
    <div class="abs res-thumb" role="img" aria-label="Scales of justice and a gavel on a table" style="background:linear-gradient(135deg,#e4e4e4,#8c7a66)"></div>
    <div class="abs res-text"><div class="date">February 28, 2024</div><h4>All the lorem ipsum generators on the internet tend.</h4><span class="link-more">Read more &#10230;</span></div>
  </div>
  <a class="abs btn res-btn">View all resources</a>
</section>

<!-- About -->
<section class="abs about" role="img" aria-label="Black and white courtroom with judge and audience">
  <div class="abs about-inner">
    <h2>About Harrowgate Trial Firm PLLC</h2>
    <p>Lorem ipsum dolor sit amet, consectetur adipiscing elit. Ut porta feugiat dolor, vel dictum eros. Cras porta diam sed est tincidunt, at placerat mi vestibulum. Duis pellentesque ut nisi sit amet auctor. Nullam dignissim dolor vel lectus dictum lacinia ut nec velit. Phasellus sollicitudin risus nec tincidunt egestas.</p>
    <a class="btn">Learn more</a>
  </div>
</section>

<!-- Reviews -->
<section class="abs reviews" role="img" aria-label="White colonnaded government buildings under a pale sky">
  <h2 class="abs section-title reviews-title">Real Customer, Real Reviews.</h2>
  <div class="abs avatar" role="img" aria-label="Reviewer portrait"></div>
  <div class="abs reviewer">
    <h4>MARCUS HALE</h4>
    <div class="stars">&#9733;&#9733;&#9733;&#9733;&#9733;</div>
    <p>"Lorem ipsum dolor sit amet, consectetur adipiscing elit. Ut porta feugiat dolor, vel dictum eros. Cras porta diam sed est tincidunt, at placerat mi vestibulum. Duis pellentesque ut nisi sit amet auctor.  Nullam dignissim dolor vel lectus dictum lacinia ut nec velit."</p>
  </div>
  <div class="abs arrow-btn" style="left:231px"><svg width="12" height="12" viewBox="0 0 12 12"><path d="M8 1 L3 6 L8 11" fill="none" stroke="#fff" stroke-width="2"/></svg></div>
  <div class="abs arrow-btn" style="left:934px"><svg width="12" height="12" viewBox="0 0 12 12"><path d="M4 1 L9 6 L4 11" fill="none" stroke="#fff" stroke-width="2"/></svg></div>
</section>

<!-- Map -->
<div class="abs map" role="img" aria-label="Street map showing the firm's office location"></div>

<!-- Footer -->
<footer class="abs footer">
  <div class="abs footer-inner">
    <div class="abs fcol" style="left:121px">
      <h5>Navigations</h5>
      <ul><li>Home</li><li>Areas of Practice</li><li>Professionals</li><li>Resources &amp; Advisories</li><li>Contact Us</li></ul>
    </div>
    <div class="abs fcol" style="left:284px">
      <h5>Contact us</h5>
      <div class="fcontact"><span class="ficon"></span><span>420 Alder Row, Suite 310,<br>Lakeport, WA 98000</span></div>
      <div class="fcontact"><span class="ficon"></span><span>(206) 555-0147</span></div>
      <div class="fcontact"><span class="ficon"></span><span style="color:var(--red)">hello@harrowgatelaw.com</span></div>
    </div>
    <div class="abs fbrand">
      <div class="brand-mark"></div>
      <div class="brand-name">HARROWGATE</div>
      <div class="brand-sub">TRIAL FIRM</div>
    </div>
    <div class="abs fcol" style="left:752px">
      <h5>Follow us</h5>
      <div class="social"><span class="ficon"></span>Friendbook</div>
      <div class="social"><span class="ficon"></span>ProLink</div>
      <div class="social"><span class="ficon"></span>Chirper</div>
    </div>
    <div class="abs fcol newsletter" style="left:887px">
      <h5>Subscribe newsletter</h5>
      <p>Enter your email below and get latest updates right int your inbox.</p>
      <div class="sub-row"><div class="sub-input"></div><a class="btn sub-btn">Subscribe</a></div>
    </div>
  </div>
  <div class="abs legal">Site Map &nbsp;|&nbsp; Privacy Policy &nbsp;|&nbsp; Terms &nbsp;|&nbsp; Copyright &copy; 2025 Harrowgate Trial Firm &nbsp;|&nbsp; All Rights Reserved.</div>
</footer>

<!-- Contact banner (sits over map and footer) -->
<section class="abs contact-box" role="img" aria-label="Red-tinted courthouse columns">
  <h2>Contact us today!</h2>
  <p>Lorem ipsum dolor sit amet, consectetur adipiscing elit. Nunc egestas efficitur interdum. Aenean mattis mauris lorem.</p>
  <a class="btn">Connect with us</a>
</section>

</body>
</html>
```